A new presentation to our clients

we are a Real Estate agency, our website is www.dorelumia.com and it’s time to have a new, fashion and remarcable Business Card. we want to differentiate ourselves from other companies so we want a business card that differentiates us. we want the business card to impact our customers. in the competitive market that we have today, we have to be different and it is this difference that we seek

Target Market(s)

Real Estate Clients

Contact Information for Business Card

We search a totaly diferent card from the usual

Font styles to use
Sans Serif

Colors
e34197

Requirements
Must have
• Logo, adress, phone contact, e-mail, photo, and our website
Nice to have
• We would like to see a modern business card
Should not have
• Houses or building draws

```html
<!DOCTYPE html>
<html lang="pt">
<head>
<meta charset="utf-8">
<title>Dore Lumia — Business Card</title>
<link href="https://fonts.googleapis.com/css2?family=Alegreya+Sans:wght@500;700&display=swap" rel="stylesheet">
<style>
  :root {
    --stage: #5e5e5e;
    --card: #ffffff;
    --magenta: #ec2a7a;
    --magenta-soft: #f7a9c8;
    --magenta-pale: #fde4ee;
  }
  html, body {
    margin: 0;
    padding: 0;
    width: 1200px;
    height: 688px;
    overflow: hidden;
    background: var(--stage);
  }
  .business-card {
    position: absolute;
    left: 83px;
    top: 59px;
    width: 1031px;
    height: 573px;
    border-radius: 40px;
    background: var(--card);
    overflow: hidden;
    font-family: "Alegreya Sans", "Segoe UI", sans-serif;
    color: var(--magenta);
  }
  .card-graphics {
    position: absolute;
    inset: 0;
  }
  .brand-name {
    position: absolute;
    right: 50px;
    top: 20px;
    margin: 0;
    font-size: 104px;
    font-weight: 500;
    line-height: 1.2;
    letter-spacing: 2px;
  }
  .contact-item {
    position: absolute;
    display: flex;
    align-items: flex-start;
    gap: 16px;
    font-size: 33px;
    font-weight: 700;
    line-height: 50px;
    margin: 0;
  }
  .contact-item svg { flex: none; fill: var(--magenta); }
  .contact-address { left: 250px; top: 215px; }
  .contact-address svg { margin-top: 20px; }
  .contact-email { left: 327px; top: 330px; }
  .contact-email svg { margin-top: 14px; }
  .contact-phone { left: 405px; top: 408px; }
  .contact-phone svg { margin-top: 12px; }
  .website {
    position: absolute;
    left: 38px;
    top: 484px;
    margin: 0;
    font-size: 56px;
    font-weight: 700;
    letter-spacing: 6px;
    line-height: 1;
  }
</style>
</head>
<body>
  <article class="business-card">
    <svg class="card-graphics" width="1031" height="573" viewBox="0 0 1031 573">
      <defs>
        <linearGradient id="swoosh-fade" x1="0" y1="0" x2="0" y2="1">
          <stop offset="0" stop-color="#ec2a7a"/>
          <stop offset="0.55" stop-color="#ec2a7a"/>
          <stop offset="1" stop-color="#ec2a7a" stop-opacity="0"/>
        </linearGradient>
        <linearGradient id="halftone-left" x1="0" y1="0" x2="1" y2="0">
          <stop offset="0" stop-color="#ec2a7a" stop-opacity="0.55"/>
          <stop offset="1" stop-color="#ec2a7a" stop-opacity="0.05"/>
        </linearGradient>
        <linearGradient id="halftone-right" x1="1" y1="0" x2="0" y2="0">
          <stop offset="0" stop-color="#ec2a7a" stop-opacity="0.6"/>
          <stop offset="1" stop-color="#ec2a7a" stop-opacity="0.04"/>
        </linearGradient>
      </defs>
      <rect class="texture-left" role="img" aria-label="Halftone dot texture fading to the right" x="0" y="150" width="215" height="330" fill="url(#halftone-left)"/>
      <rect class="texture-right" role="img" aria-label="Halftone dot texture fading to the left" x="812" y="175" width="219" height="398" fill="url(#halftone-right)"/>
      <path class="corner-swoosh" d="M0 0 H575 C420 15 275 110 205 330 L0 330 Z" fill="url(#swoosh-fade)"/>
      <path class="swoosh-highlight" d="M225 175 C205 205 190 240 178 290" stroke="#ffffff" stroke-opacity="0.55" stroke-width="6" fill="none"/>
      <rect class="dotted-frame" x="12" y="12" width="1007" height="549" rx="30" fill="none" stroke="#ec2a7a" stroke-width="2" stroke-dasharray="1 11" stroke-linecap="round"/>
    </svg>

    <h1 class="brand-name">Dore Lumia</h1>

    <p class="contact-item contact-address">
      <svg width="34" height="44" viewBox="0 0 34 44" aria-hidden="true">
        <path d="M17 0C7.6 0 0 7.4 0 16.6 0 28 17 44 17 44S34 28 34 16.6C34 7.4 26.4 0 17 0Zm0 23a6.5 6.5 0 1 1 0-13 6.5 6.5 0 0 1 0 13Z"/>
      </svg>
      <span>Rua das Flores Altas, 118<br>4410-205, Porto do Sol</span>
    </p>

    <p class="contact-item contact-email">
      <svg width="36" height="28" viewBox="0 0 36 28" aria-hidden="true">
        <path d="M0 10 18 0 36 10V28H0Z"/>
        <path d="M2 11 18 21 34 11" stroke="#ffffff" stroke-width="2.5" fill="none"/>
      </svg>
      <span>geral@dorelumia.com</span>
    </p>

    <p class="contact-item contact-phone">
      <svg width="34" height="34" viewBox="0 0 24 24" aria-hidden="true">
        <path d="M6.6 10.8a15.2 15.2 0 0 0 6.6 6.6l2.2-2.2c.3-.3.7-.4 1-.2 1.1.4 2.3.6 3.6.6.6 0 1 .4 1 1V20c0 .6-.4 1-1 1A17 17 0 0 1 3 4c0-.6.4-1 1-1h3.5c.6 0 1 .4 1 1 0 1.3.2 2.5.6 3.6.1.3 0 .7-.2 1Z"/>
      </svg>
      <span>(+351) 220 418 536</span>
    </p>

    <p class="website">www.dorelumia.com</p>
  </article>
</body>
</html>
```